Business Cards

Need a neat design for a new business card

Industry/Entity Type

Residential Construction

Contact Information for Business Card

Company Name- KOVE Construction Inc.
Owner- Marcus Tolliver
Phone number- (555)203-7481
Email- kovecohomes@brindlemail.example
Facebook- www.socialpage.example/kovecohomes

Colors
fefdec

```html
<!DOCTYPE html>
<html lang="en">
<head>
<meta charset="utf-8">
<title>KOVE Construction – Business Card</title>
<link rel="stylesheet" href="https://fonts.googleapis.com/css2?family=Montserrat:wght@500;600;700&display=swap">
<style>
  :root {
    --stage: #56575a;
    --card: #3a3a3c;
    --ink: #fefdec;
    --emboss: #2e2e30;
    --rule: #fefdec;
  }
  * { box-sizing: border-box; margin: 0; padding: 0; }
  html, body {
    width: 1200px; height: 1125px; overflow: hidden;
    background: var(--stage);
    font-family: "Montserrat", Arial, sans-serif;
  }
  .stage {
    width: 1200px; height: 1125px;
    display: flex; flex-direction: column; align-items: center; justify-content: center;
    gap: 60px;
  }
  .card {
    width: 840px; height: 480px;
    background: var(--card);
    position: relative;
    overflow: hidden;
  }

  /* Front side */
  .card-front {
    display: flex; align-items: center; justify-content: center;
  }
  .front-mark {
    display: flex; align-items: center; gap: 24px;
    color: var(--emboss);
    font-weight: 600;
  }
  .front-mark .mark-square {
    width: 30px; height: 30px; background: var(--emboss); flex: none;
  }
  .front-mark .mark-text { display: flex; flex-direction: column; align-items: center; }
  .front-mark .mark-name { font-size: 96px; letter-spacing: 10px; line-height: 1; }
  .front-mark .mark-sub { font-size: 24px; letter-spacing: 7px; margin-top: 12px; }

  /* Back side */
  .card-back {
    display: flex; align-items: center;
    padding: 0 44px 0 56px;
  }
  .brand {
    width: 290px; flex: none;
    display: flex; align-items: center; gap: 14px;
    color: var(--ink); font-weight: 500;
  }
  .brand .mark-square { width: 16px; height: 16px; background: var(--ink); flex: none; }
  .brand .brand-text { display: flex; flex-direction: column; align-items: center; }
  .brand .brand-name { font-size: 58px; letter-spacing: 6px; line-height: 1; }
  .brand .brand-sub { font-size: 14px; letter-spacing: 4px; margin-top: 8px; }
  .divider {
    width: 2px; height: 140px; background: var(--rule); margin: 0 28px 0 8px; flex: none;
  }
  .contact { color: var(--ink); min-width: 0; }
  .contact .owner {
    font-size: 25px; font-weight: 700; letter-spacing: 1.5px;
    margin-bottom: 20px;
  }
  .contact ul { list-style: none; }
  .contact li {
    display: flex; align-items: center; gap: 8px;
    font-size: 17px; font-weight: 500; letter-spacing: 0.3px;
    line-height: 29px; white-space: nowrap;
  }
  .contact svg { width: 16px; height: 16px; flex: none; fill: var(--ink); }
  .contact .social-square { width: 14px; height: 14px; background: var(--ink); flex: none; margin: 0 1px; }
</style>
</head>
<body>
<main class="stage">
  <section class="card card-front" aria-label="Card front">
    <div class="front-mark">
      <span class="mark-square"></span>
      <span class="mark-text">
        <span class="mark-name">KOVE</span>
        <span class="mark-sub">CONSTRUCTION</span>
      </span>
    </div>
  </section>

  <section class="card card-back" aria-label="Card back">
    <div class="brand">
      <span class="mark-square"></span>
      <span class="brand-text">
        <span class="brand-name">KOVE</span>
        <span class="brand-sub">CONSTRUCTION</span>
      </span>
    </div>
    <div class="divider"></div>
    <div class="contact">
      <p class="owner">MARCUS TOLLIVER</p>
      <ul>
        <li>
          <svg viewBox="0 0 24 24" aria-hidden="true"><path d="M6.6 10.8c1.4 2.8 3.8 5.1 6.6 6.6l2.2-2.2c.3-.3.7-.4 1-.2 1.1.4 2.3.6 3.6.6.6 0 1 .4 1 1V20c0 .6-.4 1-1 1C10.6 21 3 13.4 3 4c0-.6.4-1 1-1h3.5c.6 0 1 .4 1 1 0 1.3.2 2.5.6 3.6.1.3 0 .7-.2 1l-2.3 2.2z"/></svg>
          <span>(555)203-7481</span>
        </li>
        <li>
          <svg viewBox="0 0 24 24" aria-hidden="true"><path d="M3 5h18c.6 0 1 .4 1 1v.4l-10 6.3L2 6.4V6c0-.6.4-1 1-1zm-1 3.7 10 6.3 10-6.3V18c0 .6-.4 1-1 1H3c-.6 0-1-.4-1-1V8.7z"/></svg>
          <span>kovecohomes@brindlemail.example</span>
        </li>
        <li>
          <span class="social-square"></span>
          <span>/kovecohomes</span>
        </li>
      </ul>
    </div>
  </section>
</main>
</body>
</html>
```